Design for LED christmas lights

📦 Packaging Briefing – Christmas Lights (Glowna)
First design for approval – Product: 360 LED Warm White String Lights – Connectable, 8 Functions, IP44, EU Plug
🧩 Project Overview:
We are developing 6 unique box styles for the Glowna Christmas lighting range, covering 11 design variations (e.g. LED counts, lengths, plug types). This briefing is for the initial box design to be created for internal approval, based on the yellow-highlighted product in the provided Excel file.
✅ Design Style:
Use the same layout, typography, and structure as the attached LED bulb box.
The font and overall style must remain consistent with that example.
Only adjust layout elements as needed to accommodate Christmas light visuals and product-specific features.
📌 Box Content (for this product):
Product Name (front and sides):
360 LED Warm White String Lights – Connectable, 8 Functions, IP44, EU Plug
Highlight these features (icons or bullet format):
360 LEDs
Warm White
Connectable
8 Functions
IP44 (outdoor suitable)
EU Plug
Also include:
CE logo
EAN barcode (from Excel file)
Article number (from Excel file)
🖼 Visuals:
Use the corresponding product image from the Excel file.
Integrate image into the layout similarly to how the LED bulb is shown on its box (clean placement, no background clutter).
🏷 Brand & Company Info:
Brand/logo: Glowna (see attached logo file)
Company name: Brisk Harbor B.V.
Email: info@vonkelhuis.nl
Phone: +31 487 5914
🎨 Tone & Feel:
Clean, professional, and slightly festive – think minimal Christmas warmth, not overly decorative
Style should match the LED bulb box to build a coherent product line

```html
<!DOCTYPE html>
<html lang="en">
<head>
<meta charset="utf-8">
<title>Glowna 360 LED String Lights – Box Concepts</title>
<link href="https://fonts.googleapis.com/css2?family=Barlow:wght@300;400;500;700&family=Barlow+Semi+Condensed:wght@400;600;700&display=swap" rel="stylesheet">
<style>
  :root{
    --ink:#474747;
    --ink-dark:#3b3b3b;
    --amber:#f2a62a;
    --amber-soft:#f7b84a;
    --cut:#f0b44a;
    --crease:#d8333a;
    --paper:#ffffff;
    --label-grey:#c8c8c8;
  }
  html,body{margin:0;padding:0;overflow:hidden;background:var(--paper);}
  .canvas{display:block;width:1200px;height:1192px;}
  .brand{font-family:"Barlow",sans-serif;font-weight:300;letter-spacing:3px;}
  .tag{font-family:"Barlow",sans-serif;font-weight:400;letter-spacing:.4px;}
  .title{font-family:"Barlow Semi Condensed",sans-serif;font-weight:700;}
  .sub{font-family:"Barlow Semi Condensed",sans-serif;font-weight:400;letter-spacing:.5px;}
  .info{font-family:"Barlow",sans-serif;font-weight:400;}
  .concept-no{font-family:"Barlow",sans-serif;font-weight:300;fill:var(--label-grey);}
  .cut{fill:var(--paper);stroke:var(--cut);stroke-width:.8;}
  .crease{stroke:var(--crease);stroke-width:.5;fill:none;}
</style>
</head>
<body>
<svg class="canvas" viewBox="0 0 1200 1192" xmlns="http://www.w3.org/2000/svg">
  <defs>
    <radialGradient id="lightsGlow" cx="50%" cy="50%" r="55%">
      <stop offset="0" stop-color="#fff2c4"/>
      <stop offset=".45" stop-color="#f7c35a"/>
      <stop offset="1" stop-color="#f2a62a" stop-opacity="0"/>
    </radialGradient>
    <linearGradient id="amberFade" x1="0" y1="0" x2="0" y2="1">
      <stop offset="0" stop-color="#f2a62a"/>
      <stop offset=".6" stop-color="#f2a62a"/>
      <stop offset="1" stop-color="#4a4540"/>
    </linearGradient>
    <linearGradient id="cornerGlowR" x1="1" y1="0" x2="0" y2="1">
      <stop offset="0" stop-color="#f2a62a" stop-opacity=".55"/>
      <stop offset=".45" stop-color="#f2a62a" stop-opacity="0"/>
    </linearGradient>
    <linearGradient id="cornerGlowL" x1="0" y1="1" x2="1" y2="0">
      <stop offset="0" stop-color="#f2a62a" stop-opacity=".5"/>
      <stop offset=".4" stop-color="#f2a62a" stop-opacity="0"/>
    </linearGradient>
  </defs>

  <text class="concept-no" x="1140" y="80" font-size="44">1</text>
  <rect class="divider" x="0" y="590" width="1200" height="11" fill="var(--amber)"/>
  <text class="concept-no" x="1140" y="661" font-size="44">2</text>

  <!-- ============ CONCEPT 1 ============ -->
  <g class="dieline concept-1">
    <path class="cut" d="M394 284 L416 280 L416 430 L394 426 Z"/>
    <path class="cut" d="M416 430 L416 512 L472 512 L472 492 L575 492 L575 512 L630 512 L630 430"/>
    <path class="cut" d="M630 430 L630 512 L692 512 L692 482 L636 432"/>
    <path class="cut" d="M751 430 L804 490 L804 512 L910 512 L910 490 L962 432"/>
    <path class="cut" d="M962 430 L962 512 L1023 512 L1023 482 L1082 432"/>

    <path d="M416 155 Q416 134 432 134 L614 134 Q630 134 630 155 L630 280 L416 280 Z" fill="var(--ink)"/>
    <path d="M416 157 L630 157" class="crease"/>
    <rect x="416" y="180" width="214" height="100" fill="url(#cornerGlowL)" opacity=".7"/>
    <g class="lid-label" transform="rotate(180 523 215)">
      <rect x="464" y="231" width="119" height="23" rx="4" fill="var(--amber)"/>
      <text class="title" x="470" y="249" font-size="16" fill="var(--ink)">360 LED</text>
      <text class="sub" x="526" y="242" font-size="6" fill="var(--ink)">STRING LIGHTS</text>
      <text class="sub" x="526" y="250" font-size="6" fill="var(--ink)">WARM WHITE</text>
      <text class="brand" x="481" y="212" font-size="18" fill="var(--amber)">GLOWNA</text>
    </g>

    <path d="M630 280 L630 221 L740 221 L751 275 Z" fill="var(--ink)"/>
    <path d="M962 275 L972 221 L1084 221 L1084 280 Z" fill="var(--ink)"/>
    <path d="M834 280 L834 262 Q834 256 840 256 L876 256 Q882 256 882 262 L882 280 Z" fill="var(--amber)"/>

    <g class="panel front">
      <rect x="416" y="280" width="214" height="150" fill="var(--ink)"/>
      <rect x="416" y="280" width="214" height="150" fill="url(#cornerGlowR)"/>
      <text class="brand" x="433" y="318" font-size="20" fill="var(--amber)">GLOWNA</text>
      <text class="tag" x="434" y="334" font-size="7" fill="var(--amber)">YOUR LIGHT. YOUR MOMENT. GLOWNA.</text>
      <text class="tag" x="432" y="370" font-size="9" fill="#fff">12meter</text>
      <line x1="432" y1="375" x2="541" y2="375" stroke="var(--amber)" stroke-width=".6"/>
      <text class="title" x="432" y="393" font-size="17" fill="var(--amber)">360 LED</text>
      <text class="sub" x="432" y="404" font-size="9" fill="var(--amber)">WARM WHITE</text>
      <text class="sub" x="432" y="415" font-size="9" fill="var(--amber)">STRING LIGHTS</text>
      <g class="sub" font-size="5" fill="var(--amber)">
        <text x="502" y="385">• 360 LEDS</text><text x="502" y="391">• WARM WHITE</text>
        <text x="502" y="397">• CONNECTABLE</text><text x="502" y="403">• 8 FUNCTIONS</text>
        <text x="502" y="409">• IP44</text><text x="502" y="415">• EU PLUG</text>
      </g>
      <text class="info" x="576" y="416" font-size="5.5" fill="#fff">Art.no: 741508</text>
    </g>

    <g class="panel side-info">
      <rect x="630" y="280" width="121" height="150" fill="var(--ink)"/>
      <rect x="630" y="280" width="121" height="150" fill="url(#cornerGlowR)"/>
      <text class="brand" x="644" y="320" font-size="12" fill="var(--amber)">GLOWNA</text>
      <g class="info" font-size="5" fill="var(--amber)">
        <text x="651" y="331" font-weight="700">Brisk Harbor B.V.</text>
        <text x="651" y="338">Kastanjelaan 22</text>
        <text x="651" y="344">6821KL Arnhem</text>
        <text x="651" y="350">the Netherlands</text>
        <text x="651" y="362">+31 487 5914</text>
        <text x="651" y="369">info@vonkelhuis.nl</text>
        <text x="651" y="376">www.vonkelhuis.nl</text>
        <text x="644" y="388">This product shall not be disposed</text>
        <text x="644" y="394">of as unsorted municipal waste.</text>
      </g>
      <g fill="var(--amber)">
        <circle cx="646" cy="329" r="1.5"/><circle cx="646" cy="336" r="1.5"/>
        <circle cx="646" cy="360" r="1.5"/><circle cx="646" cy="367" r="1.5"/><circle cx="646" cy="374" r="1.5"/>
      </g>
      <g class="cert-marks" fill="none" stroke="#fff" stroke-width="1">
        <rect x="645" y="406" width="14" height="9"/>
        <rect x="667" y="405" width="8" height="10"/>
        <rect x="681" y="405" width="8" height="10"/>
        <path d="M696 415 L702 405 L708 415 Z"/>
      </g>
    </g>

    <g class="panel back">
      <rect x="751" y="280" width="211" height="150" fill="url(#amberFade)"/>
      <text class="brand" x="766" y="322" font-size="22" fill="#fff">GLOWNA</text>
      <rect x="766" y="333" width="55" height="33" rx="4" fill="var(--amber-soft)"/>
      <text class="title" x="770" y="347" font-size="12" fill="#fff">360 LED</text>
      <text class="sub" x="770" y="355" font-size="6.5" fill="#fff">WARM WHITE</text>
      <text class="sub" x="770" y="363" font-size="6.5" fill="#fff">STRING LIGHTS</text>
      <rect x="766" y="370" width="55" height="46" rx="4" fill="var(--amber-soft)"/>
      <g class="sub" font-size="5" fill="#fff">
        <text x="770" y="378">• 360 LEDS</text><text x="770" y="385">• WARM WHITE</text>
        <text x="770" y="392">• CONNECTABLE</text><text x="770" y="399">• 8 FUNCTIONS</text>
        <text x="770" y="406">• IP44</text><text x="770" y="413">• EU PLUG</text>
      </g>
      <rect x="830" y="318" width="128" height="108" fill="url(#lightsGlow)" role="img" aria-label="Coiled warm white LED string lights with EU plug adapter"/>
    </g>

    <g class="panel side-product">
      <rect x="962" y="280" width="122" height="150" fill="var(--ink)"/>
      <rect x="962" y="280" width="122" height="150" fill="url(#cornerGlowR)"/>
      <text class="brand" x="979" y="321" font-size="12" fill="var(--amber)">GLOWNA</text>
      <text class="title" x="979" y="343" font-size="12" fill="var(--amber)">360 LED</text>
      <text class="sub" x="979" y="352" font-size="6.5" fill="var(--amber)">WARM WHITE</text>
      <text class="sub" x="979" y="360" font-size="6.5" fill="var(--amber)">STRING LIGHTS</text>
      <g class="sub" font-size="6" fill="var(--amber)">
        <text x="979" y="375">• 360 LEDS</text><text x="979" y="383">• WARM WHITE</text>
        <text x="979" y="390">• CONNECTABLE</text><text x="979" y="398">• 8 FUNCTIONS</text>
        <text x="979" y="405">• IP44</text><text x="979" y="413">• EU PLUG</text>
      </g>
    </g>
    <path class="crease" d="M416 280 H1084 M416 430 H1084 M630 280 V430 M751 280 V430 M962 280 V430"/>
  </g>

  <!-- ============ CONCEPT 2 ============ -->
  <g class="dieline concept-2" transform="translate(0 570)">
    <path class="cut" d="M394 284 L416 280 L416 430 L394 426 Z"/>
    <path class="cut" d="M416 430 L416 512 L472 512 L472 492 L575 492 L575 512 L630 512 L630 430"/>
    <path class="cut" d="M630 430 L630 512 L692 512 L692 482 L636 432"/>
    <path class="cut" d="M751 430 L804 490 L804 512 L910 512 L910 490 L962 432"/>
    <path class="cut" d="M962 430 L962 512 L1023 512 L1023 482 L1082 432"/>

    <path d="M416 155 Q416 134 432 134 L614 134 Q630 134 630 155 L630 280 L416 280 Z" fill="var(--ink)"/>
    <path d="M416 157 L630 157" class="crease"/>
    <rect x="416" y="180" width="214" height="100" fill="url(#cornerGlowL)" opacity=".7"/>
    <g class="lid-label" transform="rotate(180 523 215)">
      <rect x="464" y="231" width="119" height="23" rx="4" fill="var(--amber)"/>
      <text class="title" x="470" y="249" font-size="16" fill="var(--ink)">360 LED</text>
      <text class="sub" x="526" y="242" font-size="6" fill="var(--ink)">STRING LIGHTS</text>
      <text class="sub" x="526" y="250" font-size="6" fill="var(--ink)">WARM WHITE</text>
      <text class="brand" x="481" y="212" font-size="18" fill="var(--amber)">GLOWNA</text>
    </g>

    <path d="M630 280 L630 221 L740 221 L751 275 Z" fill="var(--ink)"/>
    <path d="M962 275 L972 221 L1084 221 L1084 280 Z" fill="var(--ink)"/>
    <path d="M834 280 L834 262 Q834 256 840 256 L876 256 Q882 256 882 262 L882 280 Z" fill="var(--amber)"/>

    <g class="panel front">
      <rect x="416" y="280" width="214" height="150" fill="url(#amberFade)"/>
      <rect x="586" y="280" width="44" height="15" fill="var(--ink)"/>
      <text class="tag" x="589" y="291" font-size="7" fill="#fff">12 meter</text>
      <text class="brand" x="433" y="320" font-size="22" fill="#fff">GLOWNA</text>
      <text class="tag" x="434" y="331" font-size="4.5" fill="#fff">YOUR LIGHT. YOUR MOMENT. GLOWNA.</text>
      <text class="title" x="436" y="353" font-size="12" fill="#fff">360 LED</text>
      <text class="sub" x="436" y="361" font-size="6.5" fill="#fff">WARM WHITE</text>
      <text class="sub" x="436" y="369" font-size="6.5" fill="#fff">STRING LIGHTS</text>
      <rect x="432" y="373" width="49" height="46" rx="4" fill="var(--amber-soft)"/>
      <g class="sub" font-size="5" fill="#fff">
        <text x="436" y="381">• 360 LEDS</text><text x="436" y="388">• WARM WHITE</text>
        <text x="436" y="395">• CONNECTABLE</text><text x="436" y="402">• 8 FUNCTIONS</text>
        <text x="436" y="409">• IP44</text><text x="436" y="416">• EU PLUG</text>
      </g>
      <rect x="502" y="318" width="124" height="108" fill="url(#lightsGlow)" role="img" aria-label="Coiled warm white LED string lights with EU plug adapter"/>
    </g>

    <g class="panel side-info">
      <rect x="630" y="280" width="121" height="150" fill="var(--ink)"/>
      <rect x="630" y="280" width="121" height="150" fill="url(#cornerGlowR)"/>
      <g class="info" font-size="5" fill="var(--amber)">
        <text x="651" y="306" font-weight="700">Brisk Harbor B.V.</text>
        <text x="651" y="313">Kastanjelaan 22</text>
        <text x="651" y="319">6821KL Arnhem</text>
        <text x="651" y="325">the Netherlands</text>
        <text x="651" y="337">+31 487 5914</text>
        <text x="651" y="344">info@vonkelhuis.nl</text>
        <text x="651" y="351">www.vonkelhuis.nl</text>
        <text x="644" y="366" font-size="3.8">This product shall not be disposed</text>
        <text x="644" y="371" font-size="3.8">of as unsorted municipal waste.</text>
      </g>
      <line x1="644" y1="359" x2="737" y2="359" stroke="var(--amber)" stroke-width=".5"/>
      <g fill="var(--amber)">
        <circle cx="646" cy="304" r="1.5"/><circle cx="646" cy="311" r="1.5"/>
        <circle cx="646" cy="335" r="1.5"/><circle cx="646" cy="342" r="1.5"/><circle cx="646" cy="349" r="1.5"/>
      </g>
      <text class="info" x="700" y="396" font-size="4.5" fill="#fff">Art.no: 741508</text>
      <g class="cert-marks" fill="none" stroke="#fff" stroke-width="1">
        <rect x="645" y="407" width="12" height="8"/>
        <rect x="663" y="406" width="7" height="9"/>
        <rect x="675" y="406" width="7" height="9"/>
        <path d="M687 415 L692 406 L697 415 Z"/>
      </g>
    </g>

    <g class="panel back">
      <rect x="751" y="280" width="211" height="150" fill="url(#amberFade)"/>
      <rect x="919" y="280" width="43" height="15" fill="var(--ink)"/>
      <text class="tag" x="921" y="291" font-size="7" fill="#fff">12 meter</text>
      <text class="brand" x="766" y="320" font-size="22" fill="#fff">GLOWNA</text>
      <text class="tag" x="767" y="331" font-size="4.5" fill="#fff">YOUR LIGHT. YOUR MOMENT. GLOWNA.</text>
      <text class="title" x="769" y="353" font-size="12" fill="#fff">360 LED</text>
      <text class="sub" x="769" y="361" font-size="6.5" fill="#fff">WARM WHITE</text>
      <text class="sub" x="769" y="369" font-size="6.5" fill="#fff">STRING LIGHTS</text>
      <rect x="765" y="373" width="49" height="46" rx="4" fill="var(--amber-soft)"/>
      <g class="sub" font-size="5" fill="#fff">
        <text x="769" y="381">• 360 LEDS</text><text x="769" y="388">• WARM WHITE</text>
        <text x="769" y="395">• CONNECTABLE</text><text x="769" y="402">• 8 FUNCTIONS</text>
        <text x="769" y="409">• IP44</text><text x="769" y="416">• EU PLUG</text>
      </g>
      <rect x="834" y="318" width="124" height="108" fill="url(#lightsGlow)" role="img" aria-label="Coiled warm white LED string lights with EU plug adapter"/>
    </g>

    <g class="panel side-product">
      <rect x="962" y="280" width="122" height="150" fill="var(--ink)"/>
      <rect x="962" y="280" width="122" height="150" fill="url(#cornerGlowR)"/>
      <text class="brand" x="979" y="311" font-size="12" fill="var(--amber)">GLOWNA</text>
      <text class="title" x="979" y="334" font-size="12" fill="var(--amber)">360 LED</text>
      <text class="sub" x="979" y="343" font-size="6.5" fill="var(--amber)">WARM WHITE</text>
      <text class="sub" x="979" y="351" font-size="6.5" fill="var(--amber)">STRING LIGHTS</text>
      <rect x="979" y="357" width="32" height="11" rx="2" fill="var(--amber)"/>
      <text class="tag" x="982" y="365" font-size="6.5" fill="#fff">12meter</text>
      <g class="sub" font-size="6" fill="var(--amber)">
        <text x="979" y="380">• 360 LEDS</text><text x="979" y="388">• WARM WHITE</text>
        <text x="979" y="395">• CONNECTABLE</text><text x="979" y="403">• 8 FUNCTIONS</text>
        <text x="979" y="410">• IP44</text><text x="979" y="418">• EU PLUG</text>
      </g>
    </g>
    <path class="crease" d="M416 280 H1084 M416 430 H1084 M630 280 V430 M751 280 V430 M962 280 V430"/>
  </g>
</svg>
</body>
</html>
```